Management Services requires simple business card design

Business card design for a management consultancy service that we are establishing. The service will provide project-based services addressing management issues eg investigative, operational and strategic planning, library projects, reporting and customer feedback in government and local government environments. The company name will be Brantwell Management Services (or possibily just Brantwell) and the card should include two names and phones and an email address. We'd like either dark blue or red card with white text if that works??? We want SIMPLE

Industry/Entity Type

Business

```html
<!DOCTYPE html>
<html lang="en">
<head>
<meta charset="utf-8">
<title>Brantwell Management Services – Business Card</title>
<link href="https://fonts.googleapis.com/css2?family=Roboto+Condensed:wght@400;700&display=swap" rel="stylesheet">
<style>
  :root {
    --card-blue: #1667f2;
    --card-white: #ffffff;
    --backdrop: #e9ebee;
    --card-shadow: rgba(20, 30, 60, 0.22);
  }
  html, body {
    margin: 0;
    padding: 0;
    width: 1200px;
    height: 864px;
    overflow: hidden;
    background: var(--backdrop);
  }
  .canvas {
    position: relative;
    width: 1200px;
    height: 864px;
  }
  .business-card {
    position: absolute;
    left: 150px;
    top: 175px;
    width: 900px;
    height: 514px;
    background: var(--card-blue);
    box-shadow: 0 18px 40px var(--card-shadow);
    overflow: hidden;
    font-family: "Roboto Condensed", Arial, sans-serif;
    color: var(--card-white);
  }
  .accent-band {
    position: absolute;
    inset: 0;
    width: 900px;
    height: 514px;
  }
  .accent-band polygon { fill: var(--card-white); }

  .brand {
    position: absolute;
    left: 80px;
    top: 110px;
    display: flex;
    align-items: flex-end;
    gap: 14px;
  }
  .brand-name {
    font-size: 84px;
    font-weight: 700;
    line-height: 0.85;
    letter-spacing: -1px;
  }
  .brand-descriptor {
    font-size: 25px;
    font-weight: 700;
    line-height: 1.0;
    padding-bottom: 4px;
  }

  .contact {
    position: absolute;
    line-height: 1.25;
  }
  .contact-name {
    font-size: 28px;
    font-weight: 700;
    margin: 0 0 4px;
  }
  .contact-line {
    font-size: 17px;
    font-weight: 400;
    margin: 0;
  }
  .contact--on-band { left: 300px; top: 310px; color: var(--card-blue); }
  .contact--on-blue { left: 560px; top: 412px; color: var(--card-white); }
</style>
</head>
<body>
<main class="canvas">
  <section class="business-card" aria-label="Brantwell Management Services business card">
    <svg class="accent-band" viewBox="0 0 900 514" aria-hidden="true">
      <polygon points="0,360 900,180 900,330 0,510"/>
    </svg>

    <div class="brand">
      <span class="brand-name">Brantwell</span>
      <span class="brand-descriptor">Management<br>Services</span>
    </div>

    <div class="contact contact--on-band">
      <p class="contact-name">Name 1</p>
      <p class="contact-line">Phone: +123 456 7890</p>
      <p class="contact-line">email: info@brantwell.net</p>
    </div>

    <div class="contact contact--on-blue">
      <p class="contact-name">Name 2</p>
      <p class="contact-line">Phone: +123 456 7890</p>
      <p class="contact-line">email: info@brantwell.net</p>
    </div>
  </section>
</main>
</body>
</html>
```